Victory images needed for a popular solitaire game

I am looking for a "Victory" graphic that will be shown to the player after they win a game of Solitaire.

Game when playing: https://vornquell.com/playing.png
Game after winning: https://vornquell.com/won.png

Your image will replace the 'You Win' graphic.
As a 'reward' for winning, the image should feel congratulatory or celebratory.

You have full creative freedom:
* Any art/drawing style you want
* Any genre or setting you want
* Any characters you want (animal, human, other, or none)
* Any backgrounds or props you want
* Any text you want (or none)

Really your imagination is the only limit. In general fun characters or cute animals/creatures is often well received. The more fine detail in an image the better. Adding little touches into the image somewhere like card suits and what not also helps. Although I'm looking for creativity so feel free to make whatever you want that represents "victory" to you!

Your image can't have nudity or be too sexual, as it's a family friendly game.

Note: Your image will be displayed in the game on top of various textures. Your image should be in transparent PNG format. The transparent parts will reveal the game textures underneath. If your image does not have any transparency, that is ok, but you should have some sort of border or frame to help it stand out.

The final image can be any aspect ratio or resolution. The higher the resolution, the better, but it must be at least 1000 x 500

My goal is to pick MULTIPLE winners. There is no budget limit on how many winners I can choose.

Lastly if you want to 'test' how the image looks over potential in-game textures, here are two textures that are tileable/repeatable:
http://vornquell.com/woodpanel.jpg
http://vornquell.com/greenfelt.jpg

Target Market(s)

All ages and genders

Font styles to use
Decorative

Colors

Designer to choose colors to be used in the design.

Requirements
Must have
• A victorious feeling
Nice to have
• Color, characters, animals, suit symbols, etc
Should not have
• Nudity

```html
<!DOCTYPE html>
<html lang="en">
<head>
<meta charset="utf-8">
<title>You Win</title>
<link rel="stylesheet" href="https://fonts.googleapis.com/css2?family=Archivo+Black&display=swap">
<style>
  :root {
    --felt-light: #34a63e;
    --felt-mid: #22902e;
    --felt-dark: #136f20;
    --gold-top: #fff4a8;
    --gold-mid: #f3c41c;
    --gold-deep: #a8660a;
    --gold-edge: #5e3406;
    --hat-blue: #1b86d6;
    --hat-red: #df2229;
    --face-pale: #f3eee8;
    --suit-red: #e3222a;
    --suit-black: #161616;
    --star-gold: #f6c22a;
    --star-edge: #b98410;
  }
  html, body {
    margin: 0;
    padding: 0;
    width: 1200px;
    height: 903px;
    overflow: hidden;
    background: var(--felt-mid);
  }
  .victory-banner {
    position: relative;
    width: 1200px;
    height: 903px;
    background: radial-gradient(ellipse at 50% 45%, var(--felt-light) 0%, var(--felt-mid) 55%, var(--felt-dark) 100%);
  }
  .victory-banner svg {
    position: absolute;
    inset: 0;
    display: block;
  }
  .headline {
    font-family: "Archivo Black", "Arial Black", sans-serif;
    font-size: 322px;
  }
  .suit-red { fill: var(--suit-red); }
  .suit-black { fill: var(--suit-black); }
  .star { fill: var(--star-gold); stroke: var(--star-edge); stroke-width: 3; }
</style>
</head>
<body>
<main class="victory-banner">
  <svg width="1200" height="903" viewBox="0 0 1200 903">
    <defs>
      <linearGradient id="goldFill" x1="0" y1="0" x2="0" y2="1">
        <stop offset="0" stop-color="var(--gold-top)"/>
        <stop offset="0.3" stop-color="var(--gold-mid)"/>
        <stop offset="0.6" stop-color="var(--gold-deep)"/>
        <stop offset="0.82" stop-color="var(--gold-mid)"/>
        <stop offset="1" stop-color="var(--gold-top)"/>
      </linearGradient>
      <linearGradient id="jesterTone" x1="0" y1="0" x2="1" y2="1">
        <stop offset="0" stop-color="var(--hat-blue)"/>
        <stop offset="0.42" stop-color="var(--hat-blue)"/>
        <stop offset="0.58" stop-color="var(--hat-red)"/>
        <stop offset="1" stop-color="var(--hat-red)"/>
      </linearGradient>
      <radialGradient id="jesterFace" cx="0.5" cy="0.72" r="0.42">
        <stop offset="0" stop-color="var(--face-pale)" stop-opacity="0.9"/>
        <stop offset="1" stop-color="var(--face-pale)" stop-opacity="0"/>
      </radialGradient>
      <filter id="goldGlow" x="-10%" y="-20%" width="120%" height="140%">
        <feGaussianBlur in="SourceAlpha" stdDeviation="10" result="blur"/>
        <feFlood flood-color="#fff6b0" flood-opacity="0.55"/>
        <feComposite in2="blur" operator="in" result="glow"/>
        <feMerge><feMergeNode in="glow"/><feMergeNode in="SourceGraphic"/></feMerge>
      </filter>

      <path id="heart" d="M0 40 C-40 12 -50 -10 -40 -28 C-30 -46 -6 -42 0 -22 C6 -42 30 -46 40 -28 C50 -10 40 12 0 40Z"/>
      <path id="diamond" d="M0 -46 L32 0 L0 46 L-32 0Z"/>
      <path id="spade" d="M0 -46 C-10 -26 -46 -6 -42 14 C-39 32 -15 34 -4 20 L-13 44 L13 44 L4 20 C15 34 39 32 42 14 C46 -6 10 -26 0 -46Z"/>
      <g id="club">
        <circle cx="0" cy="-22" r="19"/>
        <circle cx="-22" cy="8" r="19"/>
        <circle cx="22" cy="8" r="19"/>
        <path d="M-5 0 L5 0 L13 44 L-13 44Z"/>
      </g>
      <polygon id="star" points="0,-46 13,-16 45,-14 20,7 28,40 0,22 -28,40 -20,7 -45,-14 -13,-16"/>
    </defs>

    <g class="jester" role="img" aria-label="Grinning jester head wearing a blue and red belled cap">
      <rect x="345" y="70" width="515" height="585" rx="180" fill="url(#jesterTone)" opacity="0.85"/>
      <rect x="345" y="70" width="515" height="585" rx="180" fill="url(#jesterFace)"/>
    </g>

    <g class="card-suits">
      <use href="#diamond" class="suit-red" transform="translate(268 240) rotate(20) scale(0.36)"/>
      <use href="#heart" class="suit-red" transform="translate(208 297) rotate(-15) scale(0.3)"/>
      <use href="#spade" class="suit-black" transform="translate(272 300) rotate(-15) scale(0.45)"/>
      <use href="#diamond" class="suit-red" transform="translate(326 335) rotate(-20) scale(0.4)"/>
      <use href="#spade" class="suit-black" transform="translate(152 355) rotate(30) scale(0.42)"/>
      <use href="#diamond" class="suit-red" transform="translate(205 357) rotate(15) scale(0.38)"/>
      <use href="#club" class="suit-black" transform="translate(105 430) scale(0.4)"/>
      <use href="#heart" class="suit-red" transform="translate(165 420) rotate(-20) scale(0.45)"/>
      <use href="#spade" class="suit-black" transform="translate(230 430) rotate(10) scale(0.45)"/>
      <use href="#heart" class="suit-red" transform="translate(322 425) rotate(10) scale(0.62)"/>

      <use href="#club" class="suit-black" transform="translate(948 208) scale(0.42)"/>
      <use href="#club" class="suit-black" transform="translate(905 275) scale(0.5)"/>
      <use href="#diamond" class="suit-red" transform="translate(915 338) rotate(25) scale(0.45)"/>
      <use href="#heart" class="suit-red" transform="translate(1002 325) rotate(20) scale(0.45)"/>
      <use href="#spade" class="suit-black" transform="translate(840 428) scale(0.72)"/>
      <use href="#spade" class="suit-black" transform="translate(980 383) rotate(-25) scale(0.45)"/>
      <use href="#club" class="suit-black" transform="translate(1042 383) scale(0.45)"/>
      <use href="#diamond" class="suit-red" transform="translate(1095 415) rotate(15) scale(0.4)"/>
      <use href="#heart" class="suit-red" transform="translate(985 442) rotate(25) scale(0.45)"/>
      <use href="#spade" class="suit-black" transform="translate(1052 450) rotate(-20) scale(0.42)"/>
    </g>

    <g class="stars">
      <use href="#star" class="star" transform="translate(380 202) scale(0.42)"/>
      <use href="#star" class="star" transform="translate(322 262) scale(0.5)"/>
      <use href="#star" class="star" transform="translate(262 372) scale(0.65)"/>
      <use href="#star" class="star" transform="translate(598 128) scale(0.22)"/>
      <use href="#star" class="star" transform="translate(642 120) scale(0.3)"/>
      <use href="#star" class="star" transform="translate(682 155) scale(0.38)"/>
      <use href="#star" class="star" transform="translate(833 160) scale(0.32)"/>
      <use href="#star" class="star" transform="translate(890 212) scale(0.4)"/>
      <use href="#star" class="star" transform="translate(968 272) scale(0.46)"/>
      <use href="#star" class="star" transform="translate(1070 330) scale(0.52)"/>
      <use href="#star" class="star" transform="translate(915 412) scale(0.7)"/>
    </g>

    <g class="headline" filter="url(#goldGlow)">
      <text x="75" y="700" textLength="425" lengthAdjust="spacingAndGlyphs"
            fill="url(#goldFill)" stroke="var(--gold-edge)" stroke-width="8" paint-order="stroke">YOU</text>
      <text x="680" y="700" textLength="450" lengthAdjust="spacingAndGlyphs"
            fill="url(#goldFill)" stroke="var(--gold-edge)" stroke-width="8" paint-order="stroke">WIN</text>
    </g>
  </svg>
</main>
</body>
</html>
```